Vimsa gifts app, mini-website

We have designed and launched an app to sell gift cards (a card with monetary value) and greeting cards (think penbrook paper cards made digital).

Target Market(s)

anyone who would buy and send gift cards via an app

Coding

Coded - Design and coding required

Number of Pages Required

1 page

```html
<!DOCTYPE html>
<html lang="en">
<head>
<meta charset="utf-8">
<title>Vimsa Gifts</title>
<link rel="stylesheet" href="https://fonts.googleapis.com/css2?family=Lexend:wght@400;500;600&family=Roboto:wght@400;500&display=swap">
<style>
:root{
  --red:#b3211f;
  --ink:#2f2f2f;
  --body:#6a6a6a;
  --blush:#fcf0f0;
  --card:#f6f6f6;
  --foot:#f2f2f2;
  --line:#dddddd;
  --star:#f0870f;
  --link:#2a6fd6;
}
*{box-sizing:border-box;margin:0;padding:0}
html,body{width:1200px;height:2814px;overflow:hidden;background:#fff}
body{position:relative;font-family:"Roboto",Arial,sans-serif;color:var(--ink)}
.abs{position:absolute}
.hero{left:0;top:0;width:1200px;height:543px;background:var(--blush)}
.nav a{position:absolute;top:62px;font-family:"Lexend",sans-serif;font-size:19px;color:var(--ink);text-decoration:none}
.brand{left:545px;top:20px;width:110px;height:110px;display:flex;flex-direction:column;align-items:center}
.brand-mark{width:30px;height:30px;background:var(--red);border-radius:4px;margin-top:14px}
.brand-name{margin-top:10px;font-family:"Lexend",sans-serif;font-weight:500;font-size:22px;color:var(--red);letter-spacing:1px}
.brand-sub{font-family:"Lexend",sans-serif;font-weight:500;font-size:11px;color:var(--red);letter-spacing:9px;margin-top:4px;margin-left:9px}
.fav{left:870px;top:53px;width:40px;height:42px;background:var(--red);border-radius:10px;display:flex;align-items:center;justify-content:center}
.nav-cta{left:918px;top:53px;width:152px;height:43px;background:#333;color:#fff;border-radius:22px;font-family:"Lexend",sans-serif;font-size:16px;display:flex;align-items:center;justify-content:center}
.hero-title{left:127px;top:218px;font-family:"Lexend",sans-serif;font-weight:600;font-size:54px;line-height:62px;color:var(--ink)}
.hero-cta{left:127px;top:363px;width:177px;height:48px;background:var(--red);color:#fff;border-radius:24px;font-family:"Lexend",sans-serif;font-weight:500;font-size:16px;display:flex;align-items:center;justify-content:center}
.art{border-radius:14px}
.section-title{left:0;width:1200px;text-align:center;font-family:"Lexend",sans-serif;font-weight:500;font-size:48px;color:var(--ink)}
.step-num{width:62px;height:62px;border-radius:50%;background:var(--red);color:#fff;font-family:"Lexend",sans-serif;font-size:30px;display:flex;align-items:center;justify-content:center}
.step-title{font-family:"Lexend",sans-serif;font-weight:500;font-size:35px;color:var(--ink)}
.step-text{width:430px;font-size:16px;line-height:18px;color:var(--body)}
.right{text-align:right}
.rule{height:1px;background:var(--line)}
.rev-head{left:127px;top:2140px;font-family:"Lexend",sans-serif;font-weight:500;font-size:18px}
.see-all{left:1000px;top:2146px;width:60px;text-align:right;font-size:12px;color:var(--link)}
.score{left:127px;top:2170px;font-family:"Roboto",sans-serif;font-weight:500;font-size:58px;color:#555;letter-spacing:-1px}
.score-sub{font-size:13px;color:#555}
.review{top:2278px;width:298px;height:202px;background:var(--card);border-radius:8px;padding:20px 25px}
.stars{color:var(--star);font-size:25px;letter-spacing:-1px;line-height:25px}
.reviewer{margin-top:10px;font-weight:500;font-size:16px;color:#555}
.review p{margin-top:14px;font-size:15.5px;line-height:18px;color:var(--body)}
.footer{left:0;top:2550px;width:1200px;height:264px;background:var(--foot)}
.foot-head{font-family:"Lexend",sans-serif;font-weight:500;font-size:15px;color:#222}
.badge{top:2620px;width:163px;height:47px;background:#111;border-radius:5px}
.social{top:2627px;width:39px;height:39px;border-radius:50%}
.copy{left:0;top:2752px;width:1200px;text-align:center;font-size:15px;color:#333}
</style>
</head>
<body>

<div class="abs hero"></div>
<nav class="nav">
  <a style="left:127px" href="#">Home</a>
  <a style="left:219px" href="#">How it  Works</a>
  <a style="left:384px" href="#">App</a>
</nav>
<div class="abs brand">
  <div class="brand-mark"></div>
  <div class="brand-name">Vimsa</div>
  <div class="brand-sub">GIFTS</div>
</div>
<div class="abs fav">
  <svg width="16" height="15" viewBox="0 0 16 15"><path d="M8 14 L1.5 7.5 A3.8 3.8 0 0 1 8 2.5 A3.8 3.8 0 0 1 14.5 7.5 Z" fill="#fff"/></svg>
</div>
<div class="abs nav-cta">Download App</div>
<h1 class="abs hero-title">Welcome to<br>Vimsa Gifts</h1>
<div class="abs hero-cta">Download The App</div>
<div class="abs art" role="img" aria-label="Illustration of a stack of wrapped gift boxes with ribbons and sparkles" style="left:700px;top:160px;width:455px;height:383px;border-radius:14px 14px 0 0;background:linear-gradient(135deg,#e8455a 0%,#f2c94c 45%,#5aa9e6 100%)"></div>

<h2 class="abs section-title" style="top:624px">How it works</h2>

<svg class="abs" style="left:0;top:0" width="1200" height="2000" aria-hidden="true">
  <polyline points="548,860 612,1102 560,1385 550,1410" fill="none" stroke="#e2e2e2" stroke-width="2"/>
  <polyline points="560,1510 620,1734" fill="none" stroke="#e2e2e2" stroke-width="2"/>
</svg>

<div class="abs art" role="img" aria-label="Illustration of a phone showing a contact list surrounded by gifts" style="left:222px;top:718px;width:282px;height:312px;background:linear-gradient(160deg,#dff0fb,#f7c7d3 60%,#f4b65c)"></div>
<div class="abs step-num" style="left:517px;top:799px">1</div>
<div class="abs step-title" style="left:603px;top:800px">Pick a recipient</div>
<div class="abs step-text" style="left:605px;top:855px">Lorem ipsum dolor sit amet, consectetur adipiscing elit, sed do eiusmod tempor incididunt ut labore et dolore magna aliqua. Quis ipsum suspendisse ultrices gravida. Risus commodo viverra maecenas accumsan lacus vel facilisis.</div>

<div class="abs art" role="img" aria-label="Illustration of friends with greeting cards and gifts" style="left:718px;top:1015px;width:296px;height:296px;background:linear-gradient(160deg,#f8ecd0,#f2c94c 50%,#e8455a)"></div>
<div class="abs step-num" style="left:590px;top:1102px">2</div>
<div class="abs step-title right" style="left:171px;top:1102px;width:400px">Pick a greeting card</div>
<div class="abs step-text right" style="left:141px;top:1157px">Lorem ipsum dolor sit amet, consectetur adipiscing elit, sed do eiusmod tempor incididunt ut labore et dolore magna aliqua. Quis ipsum suspendisse ultrices gravida. Risus commodo viverra maecenas accumsan lacus vel facilisis.</div>

<div class="abs art" role="img" aria-label="Illustration of a phone gift card shop with shoppers and gift boxes" style="left:145px;top:1320px;width:395px;height:325px;background:linear-gradient(150deg,#e8455a,#fbd88a 45%,#5aa9e6)"></div>
<div class="abs step-num" style="left:518px;top:1409px">3</div>
<div class="abs step-title" style="left:604px;top:1410px">Add a gift card</div>
<div class="abs step-text" style="left:605px;top:1463px">Lorem ipsum dolor sit amet, consectetur adipiscing elit, sed do eiusmod tempor incididunt ut labore et dolore magna aliqua. Quis ipsum suspendisse ultrices gravida. Risus commodo viverra maecenas accumsan lacus vel facilisis.</div>

<div class="abs art" role="img" aria-label="Illustration of a shopper pushing a cart full of gifts" style="left:725px;top:1690px;width:300px;height:215px;background:linear-gradient(150deg,#f2c94c,#7ac4ef 45%,#e8455a)"></div>
<div class="abs step-num" style="left:590px;top:1734px">4</div>
<div class="abs step-title right" style="left:171px;top:1734px;width:400px">Checkout</div>
<div class="abs step-text right" style="left:141px;top:1789px">Lorem ipsum dolor sit amet, consectetur adipiscing elit, sed do eiusmod tempor incididunt ut labore et dolore magna aliqua. Quis ipsum suspendisse ultrices gravida. Risus commodo viverra maecenas accumsan lacus vel facilisis.</div>

<h2 class="abs section-title" style="top:2020px">Read the reviews</h2>
<div class="abs rule" style="left:127px;top:2122px;width:933px"></div>
<div class="abs rev-head">Ratings and Reviews</div>
<div class="abs see-all">See All</div>
<div class="abs score">5.0 <span class="score-sub">out of 5</span></div>
<div class="abs score-sub" style="left:355px;top:2210px">264 Ratings</div>
<svg class="abs" style="left:443px;top:2180px" width="300" height="45" aria-hidden="true">
  <g fill="#888">
    <rect x="2" y="2" width="44" height="3"/><rect x="8" y="10" width="38" height="3"/><rect x="20" y="18" width="26" height="3"/><rect x="32" y="26" width="14" height="3"/><rect x="40" y="34" width="6" height="3"/>
  </g>
  <g stroke-width="1.5">
    <line x1="56" y1="4" x2="298" y2="4" stroke="#666"/>
    <line x1="56" y1="12" x2="298" y2="12" stroke="#e6e6e6"/>
    <line x1="56" y1="20" x2="298" y2="20" stroke="#e6e6e6"/>
    <line x1="56" y1="28" x2="298" y2="28" stroke="#e6e6e6"/>
    <line x1="56" y1="36" x2="298" y2="36" stroke="#e6e6e6"/>
  </g>
</svg>

<div class="abs review" style="left:127px">
  <div class="stars">★★★★★</div>
  <div class="reviewer">Maren Holt</div>
  <p>Lorem ipsum dolor sit amet, con se ctetur adipiscing elit, sed do eiusmod tempor incididunt ut labore et dolore magna aliqua. Quis ipsulores uspen disse ultrices gravida.</p>
</div>
<div class="abs review" style="left:451px">
  <div class="stars">★★★★★</div>
  <div class="reviewer">Maren Holt</div>
  <p>Lorem ipsum dolor sit amet, con se ctetur adipiscing elit, sed do eiusmod tempor incididunt ut labore et dolore magna aliqua. Quis ipsulores uspen disse ultrices gravida.</p>
</div>
<div class="abs review" style="left:773px">
  <div class="stars">★★★★★</div>
  <div class="reviewer">Maren Holt</div>
  <p>Lorem ipsum dolor sit amet, con se ctetur adipiscing elit, sed do eiusmod tempor incididunt ut labore et dolore magna aliqua. Quis ipsulores uspen disse ultrices gravida.</p>
</div>

<footer class="abs footer"></footer>
<div class="abs foot-head" style="left:131px;top:2586px">Download our Vimsa app for a better experience !!</div>
<div class="abs badge" style="left:131px" role="img" aria-label="Store download badge"></div>
<div class="abs badge" style="left:341px" role="img" aria-label="Store download badge"></div>
<div class="abs foot-head" style="left:786px;top:2586px;width:200px;text-align:center">Follow Us</div>
<div class="abs social" style="left:763px;background:#3b5998" role="img" aria-label="Social link"></div>
<div class="abs social" style="left:819px;background:#1da1f2" role="img" aria-label="Social link"></div>
<div class="abs social" style="left:874px;background:#e1306c" role="img" aria-label="Social link"></div>
<div class="abs social" style="left:929px;background:#0077b5" role="img" aria-label="Social link"></div>
<div class="abs social" style="left:985px;background:#e62117" role="img" aria-label="Social link"></div>
<div class="abs rule" style="left:127px;top:2706px;width:946px;background:#dcdcdc"></div>
<div class="abs copy">Copyright © 2023 Vimsa. All rights reserved.</div>

</body>
</html>
```